Franchising Brochure Design Project

We need a serious revamp of our in-house made Franchising Brochure, which currently has 10 pages (possibly due to the way text was laid out).

VelmoraHUB has recently started a rebranding project and we would like to find a suitable designer to help us going through this journey. This is the least technical document and we feel it would be a good start.

We are looking for a bold yet stylish redesign of this document, which should appeal to a global audience, as does our business opportunity.

For the deadline we would like to see a couple pages 3-4 maximum using some of the content we provide.

Target Market(s)

International English-speaking expats who want to set up their own business in international locations around the world.

Industry/Entity Type

Business

Requirements
Must have
• Must be delivered in InDesign or another editable format, as well as High Res PDF

Good imagery - we can help source

```html
<!DOCTYPE html>
<html lang="en">
<head>
<meta charset="utf-8">
<title>VelmoraHUB Franchising – Next steps</title>
<link rel="stylesheet" href="https://fonts.googleapis.com/css2?family=Arimo:wght@400;700&family=EB+Garamond:wght@400;500&display=swap">
<style>
  :root {
    --brand-red: #b5261e;
    --band-red: #c2462c;
    --panel-fill: rgba(244, 240, 236, 0.86);
    --ink: #231f1c;
    --paper: #ffffff;
    --footer-text: #e9e2da;
  }
  *, *::before, *::after { box-sizing: border-box; margin: 0; padding: 0; }
  html, body {
    width: 1200px; height: 1200px; overflow: hidden;
    background: var(--paper);
  }
  .spread {
    position: absolute; left: 60px; top: 218px;
    width: 1080px; height: 764px; overflow: hidden;
    box-shadow: 0 0 0 1px rgba(0,0,0,0.08);
  }
  .scene-photo {
    position: absolute; inset: 0;
    background:
      radial-gradient(ellipse 38% 55% at 78% 58%, rgba(150,110,75,0.55), rgba(150,110,75,0) 70%),
      linear-gradient(180deg, #d9c3a3 0%, #e6d2b4 22%, #d6c4ad 30%, #a79a8c 36%, #8f877d 55%, #7d7268 72%, #6e5d4d 86%, #5a4a3c 100%);
  }
  .side-band {
    position: absolute; top: 0; right: 0; width: 74px; height: 100%;
    background: var(--band-red);
    opacity: 0.92;
  }
  .info-panel {
    position: absolute; left: 52px; top: 108px;
    width: 456px; height: 510px;
    background: var(--panel-fill);
    border: 1.5px solid var(--brand-red);
    border-radius: 12px;
    padding: 14px 16px 0 20px;
    overflow: hidden;
  }
  .panel-title {
    font-family: "Arimo", Arial, sans-serif;
    font-weight: 700; font-size: 23px; line-height: 26px;
    color: var(--brand-red);
    margin-bottom: 4px;
  }
  .panel-intro, .step-list li {
    font-family: "EB Garamond", Garamond, serif;
    font-size: 14.3px; color: var(--ink);
  }
  .panel-intro { line-height: 22px; margin-bottom: 4px; }
  .step-list { list-style: none; }
  .step-list li {
    position: relative; padding-left: 16px; margin-bottom: 7px;
    line-height: 20px;
  }
  .step-list li::before {
    content: ""; position: absolute; left: 0; top: 6px;
    width: 9px; height: 9px; border-radius: 50%;
    border: 2.5px solid var(--brand-red); background: #fff;
  }
  .call-to-action {
    font-family: "Arimo", Arial, sans-serif;
    font-weight: 700; font-size: 15px; line-height: 18px;
    color: var(--brand-red);
    margin-top: 11px;
  }
  .photo-strip {
    position: absolute; left: 20px; right: 16px; bottom: 17px;
    display: flex; gap: 3px;
  }
  .photo-strip .thumb { flex: 1; height: 111px; }
  .thumb-couple { background: linear-gradient(160deg, #b9a27c, #8a7658 60%, #d8cfc2); }
  .thumb-beach { background: linear-gradient(180deg, #7fb2cf 0%, #b9d3dc 45%, #e0cfae 70%, #d2b98e 100%); }
  .thumb-office { background: linear-gradient(150deg, #e7e4dc, #c9c2b3 55%, #f1efe9); }
  .footer-name {
    position: absolute; left: 29px; bottom: 16px;
    font-family: "Arimo", Arial, sans-serif; font-size: 13.5px;
    color: var(--footer-text);
  }
  .page-number {
    position: absolute; right: 27px; bottom: 14px;
    font-family: "Arimo", Arial, sans-serif; font-weight: 700; font-size: 16px;
    color: #fff;
  }
</style>
</head>
<body>
  <main class="spread">
    <div class="scene-photo" role="img" aria-label="Photograph of a calm sea at sunset with a pebble shore, and a grey-haired person holding a large conch shell to their ear"></div>
    <div class="side-band"></div>

    <section class="info-panel">
      <h2 class="panel-title">Next steps</h2>
      <p class="panel-intro">Once you have had an opportunity to assess your interest in the franchise in more detail (based on this document and your own initial research) we proceed as follows:</p>
      <ul class="step-list">
        <li>You sign a nondisclosure agreement (NDA) with us.</li>
        <li>We handle your more detailed questions both in writing and over the telephone.</li>
        <li>We supply draft copies of the Franchisee Contract, a Disclosure Document and give you access to the VelmoraHUB Manual.</li>
        <li>You have the opportunity to speak to existing VelmoraHUB franchisees in order to see the process from their perspective.</li>
      </ul>
      <p class="call-to-action">Being an VelmoraHUB franchisee is an exciting prospect – being your own boss, running your own business wherever you want to be in the world. Why not grasp the opportunity now?</p>
      <div class="photo-strip">
        <div class="thumb thumb-couple" role="img" aria-label="Photograph of an older couple working together on a laptop at home"></div>
        <div class="thumb thumb-beach" role="img" aria-label="Photograph of a family running hand in hand along a sunny beach"></div>
        <div class="thumb thumb-office" role="img" aria-label="Photograph of a woman on the phone at a bright home office desk"></div>
      </div>
    </section>

    <p class="footer-name">VelmoraHUB Franchising</p>
    <p class="page-number">4</p>
  </main>
</body>
</html>
```